Existing Wix Website Redesign

Our current website is in need of redesign for the wix.com platform. https://www.brackettrails.com.au/ <br/>In addition to the brief below, we need the Website to be Multi – Lingual : English, Japanese, German, Dutch, French, Italian, Chinese Mandarin and Chinese Cantonese & Korean<br/><br/>All the content is already listed on the website. The successful design will implement the website with the current content and edit this including correct headers and URL addresses.<br/><br/>Company Profile-<br/>Orwell’s Treks enhances the travellers' life experience through the wonder, discovery, adventure and cultural immersion of high quality tours throughout Papua New Guinea.<br/><br/>Our mission is to design and conduct safe, educational and exciting tours which:<br/><br/>cater for a range of ages, interests and budgets; respect local communities; promote sustainable tourism, leaving with them special memories.<br/><br/> <br/><br/>The current target demographic for Orwell’s Treks of Papua New Guinea is the 50+ age group, primarily in Australia and New Zealand, but also the United States, Japan, Europe (Germany, France Italy & Britain and also China as it’s outbound visitor market matures and seeks new adventures.<br/><br/>We offer fully escorted small group tours and holidays that are safe, fully organised and guided for all age groups, nationalities and budgets.<br/><br/>PNG is uniquely placed as an attractive destination, showcasing the oldest, authentic surviving culture on earth! <br/><br/>Over 800 tribes generously share their customs, art, music, carvings, costumes and dances at a range of Festivals or “sing sings” held across the highlands and islands of this most picturesque of countries providing visiting culture enthusiasts and photographers with lasting memories and vivid images. Traversing the Pacific’s “Rim of Fire”, visitors are presented with a daily feast of scenery with the best nature has to offer amongst it’s big mountainous jungles and forests, untamed rivers, volcanic landscapes and pristine marine environments. Photograph animals, plants and exotic birds including the globally renowned Birds of Paradise.<br/><br/>The key group to target amongst the over 50’s are the Baby Boomers who are those born between 1946 to 1964.<br/><br/> <br/><br/>Baby boomers are also seeking an authentic experience whilst travelling. They want to go where the locals go, immersing themselves fully to experience and learn about a new culture.<br/><br/>According to the Global Voyage Council, boomers are more likely to seek out educational and cultural experiences. What boomers really want is to be intellectually stimulated, which is why an experienced, knowledgeable and well-trained guide, such as Peter Mallory and those guides that he trains are necessary to attract them to these tours. Peter has immersed himself in the many periods of colonial occupier history along with a sound understanding of the first peoples and their cultures and Melanesian lifestyles.<br/><br/>As a destination Papua New Guinea will attract the baby boomers that are “young at heart” who actively seek out adventure, sometimes as a form of self-discovery. Knowing that they want to experience new adventures while being safe, Orwell’s Treks has created adventure in a semi-controlled environment for the baby boomer.<br/><br/>Orwell’s Treks of Papua New Guinea will be of interest primarily to the “Baby Boomer” demographic in Australia, many who have a fond familiarity with their neighbouring ex-colony. Their parents may have been involved in PNG in the pre-independence era as First and Second World War military personal, “Kiap” patrol officers, nurses, teachers,missionaries, tradesmen or public servants.<br/><br/>Potential visitors will discover a little known destination where the traditional Melanesian culture with over 800 tribes and languages, thrive and where, outside the major regional centres, little has changed in thousands of years.

Target Market(s)

Travel and Tourism

Colors

Designer to choose colors to be used in the design.

Requirements
Must have
• Website to be Multi – Lingual : English, Japanese, German, Dutch, French, Italian, Chinese Mandarin and Chinese Cantonese & Korean
• The successful design will implement the website with the current content and edit this including correct headers and URL addresses.

```html
<!DOCTYPE html>
<html lang="en">
<head>
<meta charset="utf-8">
<title>Orwell’s Treks of Papua New Guinea</title>
<link href="https://fonts.googleapis.com/css2?family=Mulish:wght@400;600;700&family=Oswald:wght@400&display=swap" rel="stylesheet">
<style>
:root{
  --ink:#1f1f1f;
  --text:#333;
  --muted:#555;
  --header:#f5f5f5;
  --band:#ececec;
  --dark:#2e2e2e;
  --darker:#262626;
  --white:#fff;
  --line:#dcdcdc;
}
*{box-sizing:border-box;margin:0;padding:0}
html,body{width:1200px;height:4584px;overflow:hidden}
body{position:relative;font-family:'Mulish',sans-serif;color:var(--text);background:var(--white)}
.abs{position:absolute}
.site-header{left:0;top:0;width:1200px;height:98px;background:var(--header);border-bottom:1px solid #e2e2e2}
.brand{left:90px;top:18px;display:flex;align-items:center;gap:10px}
.brand-mark{width:40px;height:40px;border:2px solid var(--ink);border-radius:50%}
.brand-name{font-family:'Oswald',sans-serif;font-size:26px;color:var(--ink);line-height:1}
.brand-sub{font-family:'Oswald',sans-serif;font-size:12px;color:var(--ink);display:block;margin-top:3px}
.main-nav{left:323px;top:38px;display:flex;gap:0;font-size:16px;color:#444}
.main-nav a{color:#444;text-decoration:none;position:absolute;white-space:nowrap}
.main-nav a.active{color:var(--ink);font-weight:600;text-decoration:underline;text-underline-offset:4px}
.social-dots{display:flex;gap:16px}
.dot{width:14px;height:14px;border-radius:50%;background:#333;display:inline-block}
.hero{left:0;top:98px;width:1200px;height:538px;background:linear-gradient(180deg,#9aa0a3 0%,#b9bcbc 35%,#7c8790 62%,#3d4a3a 80%,#2a3024 100%)}
.hero-brand{left:90px;top:270px;display:flex;align-items:center;gap:12px}
.hero-brand .brand-mark{width:70px;height:70px;border-color:#2a2a2a}
.hero-brand .brand-name{font-size:52px;color:#2a2a2a}
.hero-brand .brand-sub{font-size:22px;color:#2a2a2a}
.hero-tag{left:90px;top:392px;font-size:28px;line-height:42px;color:#f4f4f4;letter-spacing:.5px}
.section-title{width:1200px;left:0;text-align:center;font-size:36px;font-weight:600;color:var(--ink)}
.about-text{left:135px;top:770px;width:930px;text-align:center;font-size:17px;line-height:36px;color:var(--text)}
.photo{position:absolute}
.band{left:0;top:1271px;width:1200px;height:216px;background:var(--band)}
.featured-label{left:90px;top:1362px;font-size:28px;color:var(--ink)}
.badge{top:1337px;width:191px;height:84px;background:var(--white);border:1px solid #d8d8d8;display:flex;align-items:center;justify-content:center}
.badge span{width:90px;height:40px;border-radius:20px;background:#bdbdbd}
.avatar{width:100px;height:100px;border-radius:50%;background:#222;display:flex;align-items:center;justify-content:center}
.author{font-size:28px;color:var(--ink)}
.post-date{font-size:17px;font-weight:700;color:var(--ink)}
.post-title{font-size:28px;font-weight:600;color:var(--ink)}
.post-body{left:90px;width:1020px;font-size:15.5px;line-height:36px;color:var(--text);text-align:justify}
.divider{left:90px;width:1020px;height:1px;background:var(--line)}
.meta{left:90px;width:1020px;font-size:16px;color:#444;display:flex;justify-content:space-between}
.social-bar{left:0;top:3800px;width:1200px;height:91px;background:var(--dark);color:#eee;font-size:18px}
.social-bar span{position:absolute;top:34px;display:flex;align-items:center;gap:6px}
.social-bar i{width:12px;height:12px;border-radius:50%;background:#eee;display:inline-block}
.footer{left:0;top:4156px;width:1200px;height:428px;background:var(--dark);color:#eee}
.footer h3{font-size:28px;font-weight:400;color:#f2f2f2}
.footer p{font-size:12px;line-height:26px;color:#ddd;text-align:justify}
.email{left:768px;top:4323px;width:342px;height:50px;background:var(--white);color:#999;font-size:15px;padding:15px 14px}
.subscribe{left:768px;top:4390px;width:342px;height:50px;border:1px solid #eee;color:#f2f2f2;font-size:18px;text-align:center;line-height:48px}
.copyright{left:90px;top:4540px;font-size:13px;color:#eee}
</style>
</head>
<body>

<header class="site-header abs">
  <div class="brand abs">
    <span class="brand-mark"></span>
    <div><span class="brand-name">Orwell’s Treks</span><span class="brand-sub">of Papua New Guinea</span></div>
  </div>
  <nav class="main-nav abs">
    <a class="active" style="left:0">HOME</a>
    <a style="left:82px">Tours</a>
    <a style="left:155px">Bird Watching</a>
    <a style="left:295px">Gallery</a>
    <a style="left:382px">About Us</a>
    <a style="left:485px">Contact</a>
    <a style="left:582px">● EN ▾</a>
  </nav>
  <div class="social-dots abs" style="left:995px;top:41px"><i class="dot"></i><i class="dot"></i><i class="dot"></i><i class="dot"></i></div>
</header>

<section class="hero abs" role="img" aria-label="Mountain castle with snowy peaks behind and trees in the foreground">
</section>
<div class="hero-brand abs">
  <span class="brand-mark"></span>
  <div><span class="brand-name">Orwell’s Treks</span><span class="brand-sub">of Papua New Guinea</span></div>
</div>
<p class="hero-tag abs">Fully Escorted Small Group Tours<br>Safe Adventures of Papua New Guinea</p>

<h2 class="section-title abs" style="top:718px">About Orwell’s Treks</h2>
<p class="about-text abs">Orwell’s Treks is a tour operator specialising in Papua New Guinea and also Japan. All our destinations offer the ultimate experience for excitement, fun, adventure and cultural interaction. Come and discover the ancient lands and first peoples, experiencing up close the vividly spectacular and varied forms of customs, art, costumes and cuisine in the most culturally intact places in the world.</p>
<div class="photo" style="left:90px;top:931px;width:331px;height:245px;background:linear-gradient(135deg,#8d8a86,#5c6a52)" role="img" aria-label="Mudmen in clay masks among tropical plants"></div>
<div class="photo" style="left:434px;top:931px;width:331px;height:245px;background:radial-gradient(circle at 45% 55%,#f6c24a,#c4511a 45%,#3a1a0c)" role="img" aria-label="Fire dancer in a painted mask at night"></div>
<div class="photo" style="left:778px;top:931px;width:332px;height:245px;background:linear-gradient(135deg,#3f5a2a,#8a5a3a 60%,#2f4a22)" role="img" aria-label="Highland man with painted face and a child"></div>

<section class="band abs"></section>
<p class="featured-label abs">As Featured in</p>
<div class="badge abs" style="left:325px"><span></span></div>
<div class="badge abs" style="left:523px"><span></span></div>
<div class="badge abs" style="left:721px"><span></span></div>
<div class="badge abs" style="left:919px"><span></span></div>

<h2 class="section-title abs" style="top:1573px">Our Blog</h2>

<article>
  <div class="photo" style="left:90px;top:1659px;width:1020px;height:483px;background:linear-gradient(90deg,#b7c6dc 0%,#e4ecf4 40%,#d2dceb 60%,#f0f3f7 100%)" role="img" aria-label="Bus driving between towering snow walls on a mountain road"></div>
  <div class="avatar abs" style="left:90px;top:2177px"><svg width="48" height="48" viewBox="0 0 48 48"><circle cx="24" cy="15" r="10" fill="#fff"/><path d="M4 46c0-12 9-18 20-18s20 6 20 18z" fill="#fff"/></svg></div>
  <p class="author abs" style="left:203px;top:2193px">Admin ♛</p>
  <p class="post-date abs" style="left:203px;top:2236px">October 27, 2016 &nbsp;|&nbsp; 6 min</p>
  <h3 class="post-title abs" style="left:90px;top:2302px">The Mighty Sepik River</h3>
  <p class="post-body abs" style="top:2354px">We journeyed down the mysterious Sepik River in a motorised dugout canoe, experiencing traditional village life along the way. Local villagers have lived along the river for millennia producing magnificent wood carvings and artful clay pottery. Ecologically, the Sepik River system is possibly the largest uncontaminated freshwater wetland system in the Asia-Pacific region. The river dominates the north-east region of PNG and the crocodiles that inhabit it, are central to the animist beliefs and initiation ceremonies that are still practised in this remote part of the world.Travelling on the Sepik River in a canoe is safe and provides an ideal vantage point from which to observe the river’s aquatic inhabitants, abundant birdlife and Sepik River peoples whose daily life seems unchanged by modernity. (Crocodiles pose no threat to tourists. The introduction of boat motors in recent decades has pushed the crocodile population away from the main Sepik River into its tributaries and extensive lake system).</p>
  <div class="divider abs" style="top:2658px"></div>
  <div class="meta abs" style="top:2680px"><span>● 208 views &nbsp;&nbsp;| &nbsp;&nbsp;● Write a comment</span><span>♥ 17</span></div>
</article>

<article>
  <div class="photo" style="left:90px;top:2774px;width:1020px;height:484px;background:linear-gradient(180deg,#c9c6be 0%,#8e8c84 45%,#4d5e3a 80%,#2f4a24 100%)" role="img" aria-label="Three men standing beside an old aircraft wreck in the jungle"></div>
  <div class="avatar abs" style="left:90px;top:3294px"><svg width="48" height="48" viewBox="0 0 48 48"><circle cx="24" cy="15" r="10" fill="#fff"/><path d="M4 46c0-12 9-18 20-18s20 6 20 18z" fill="#fff"/></svg></div>
  <p class="author abs" style="left:203px;top:3310px">Admin ♛</p>
  <p class="post-date abs" style="left:203px;top:3353px">October 27, 2016 &nbsp;|&nbsp; 6 min</p>
  <h3 class="post-title abs" style="left:90px;top:3419px">Bougainville - nature survived in war zone</h3>
  <p class="post-body abs" style="top:3472px">Bougainville is an ecological wonderland where you can -immerse yourself in the splendor of its natural and scenic beauty. The civil war of the 1990s had kept loggers away and habitats relatively intact. Professor Tom Fenwick, one of the world’s leading experts on mammals of Melanesia, regards this region as “the Galápagos of the Western Pacific”. The island is dotted with bat filled caves, caldera lakes and giant sinkholes including the largest cavern in the world. There are a great variety of tropical birds on Bougainville, which makes it the perfect place for birdwatching.</p>
  <div class="divider abs" style="top:3667px"></div>
  <div class="meta abs" style="top:3688px"><span>● 208 views &nbsp;&nbsp;| &nbsp;&nbsp;● Write a comment</span><span>♥ 17</span></div>
</article>

<section class="social-bar abs">
  <span style="left:178px"><i></i>Facepage</span>
  <span style="left:428px"><i></i>Snapgram</span>
  <span style="left:688px"><i></i>Pinboard</span>
  <span style="left:938px"><i></i>Chirper</span>
</section>
<div class="photo" style="left:0;top:3891px;width:240px;height:265px;background:linear-gradient(135deg,#2f8a2a,#6bbf3a 50%,#c0202a)" role="img" aria-label="Green and red parrots on a branch"></div>
<div class="photo" style="left:240px;top:3891px;width:240px;height:265px;background:linear-gradient(180deg,#9fb48a,#4d5e3a 60%,#3a3024)" role="img" aria-label="Traditional thatched house among palms"></div>
<div class="photo" style="left:480px;top:3891px;width:240px;height:265px;background:radial-gradient(circle at 40% 40%,#e8e0dc,#c8262a 60%,#8c1418)" role="img" aria-label="Geisha with a red patterned parasol"></div>
<div class="photo" style="left:720px;top:3891px;width:240px;height:265px;background:linear-gradient(135deg,#3b4f2a,#b8403a 50%,#2a3a20)" role="img" aria-label="Painted ceremonial mask with feathers"></div>
<div class="photo" style="left:960px;top:3891px;width:240px;height:265px;background:linear-gradient(135deg,#2f5a22,#d9a030 50%,#b8302a)" role="img" aria-label="Child in a feathered festival headdress"></div>

<footer class="footer abs">
  <p class="abs" style="left:0;width:1200px;top:42px;text-align:center;font-size:17px;color:#eee">Show More</p>
  <div class="photo" style="left:90px;top:101px;width:251px;height:219px;background:linear-gradient(180deg,#2a8fd0,#1a6aa8 55%,#c0603a)" role="img" aria-label="Coral reef with tropical fish"></div>
  <h3 class="abs" style="left:364px;top:110px">About Us</h3>
  <p class="abs" style="left:360px;top:160px;width:362px">Lorem ipsum dolor sit amet, consectetur adipiscing elit, sed do eiusmod tempor incididunt ut labore et dolore magna aliqua. Quis ipsum suspendisse ultrices gravida. Risus commodo viverra maecenas accumsan lacus vel facilisis.</p>
  <p class="abs" style="left:364px;top:278px;font-size:18px;text-decoration:underline">Read More</p>
  <h3 class="abs" style="left:768px;top:110px">Join My Mailing List</h3>
</footer>
<div class="email abs">Enter Email</div>
<div class="subscribe abs">Subscribe Now</div>
<p class="copyright abs">© 2019 Orwell’s Treks. All Rights are Reserved</p>
<div class="abs" style="left:995px;top:4542px;display:flex;gap:16px"><i class="dot" style="background:#eee"></i><i class="dot" style="background:#eee"></i><i class="dot" style="background:#eee"></i><i class="dot" style="background:#eee"></i></div>

</body>
</html>
```